A business card design for a dental office. We have Two doctors working here. We practice general de

I already have a logo designed for the office with the name and a slogan.
Now I need to create design for a business card using the same logo.
Details Needed on the front side of the card are :
Gerald K. Voskamp, DDS
Marvin R Duchene, DDS
418 Birchwood Lane
Portland, CT 06591
Phone : 860 517 4093
Fax : 860 517 4094
Website : WWW.BrightArcDental.Com
Office hours by appointment
On the back side of the card need :
Appointment
Date....................Time...................
With....................................
If unable to keep your appointment, please give 24-48 hours notice in order to avoid broken appointment fee.

Industry/Entity Type

Dental Clinic

Contact Information for Business Card

Gerald K. Voskamp, DDS
Marvin R Duchene, DDS
418 Birchwood Lane
Portland, CT 06591
Phone : 860 517 4093
Fax : 860 517 4094
Appointment

Requirements
Must have
• Keep the Name and slogan on the logo on the front of the card. You can move them around the Logo and Name/Slogan of business (Voskamp Family Dentistry/We give you reasons to smile) as you wish to get a feel of the design.
• Gerald K. Voskamp, DDS
• Marvin R Duchene, DDS
• 418 Birchwood Lane
• Portland, CT 06591
• Phone : 860 517 4093
• Fax : 860 517 4094
• WWW.BrightArcDental.Com
• Keep these three groups above as they are together now in different areas of the front side.
• On the back side of the card need :
• Appointment
• Date....................Time...................
• With....................................
• If unable to keep your appointment, please give 24-48 hours notice in order to avoid broken appointment fee.

```html
<!DOCTYPE html>
<html lang="en">
<head>
<meta charset="utf-8">
<title>Voskamp Family Dentistry – Business Card</title>
<link rel="stylesheet" href="https://fonts.googleapis.com/css2?family=Open+Sans:wght@400;600;700&display=swap">
<style>
  :root {
    --bg: #8f8f8f;
    --paper: #ffffff;
    --ink-blue: #1f4e9c;
    --ink-red: #e0242f;
    --dot-blue: #2a57a8;
    --night: #000000;
    --teal: #14a889;
    --red: #e3262f;
    --sky-top: #9cc3ea;
    --sky-bottom: #1d5aa6;
    --white: #ffffff;
  }
  * { box-sizing: border-box; margin: 0; padding: 0; }
  html, body { width: 1200px; height: 900px; overflow: hidden; }
  body {
    background: var(--bg);
    font-family: "Open Sans", sans-serif;
    position: relative;
  }
  .card {
    position: absolute;
    left: 260px;
    width: 680px;
    height: 389px;
    overflow: hidden;
    box-shadow: 0 6px 18px rgba(0,0,0,0.25);
  }
  /* Back side: appointment card */
  .card-back { top: 40px; background: var(--paper); }
  .brand {
    position: absolute;
    top: 42px;
    left: 0; right: 0;
    display: flex;
    align-items: center;
    justify-content: center;
    gap: 14px;
  }
  .brand-dot {
    width: 58px; height: 58px;
    border-radius: 50%;
    background: var(--ink-blue);
  }
  .brand-name {
    color: var(--ink-blue);
    font-weight: 700;
    font-size: 24px;
    letter-spacing: 2px;
    text-transform: uppercase;
  }
  .appt-title {
    position: absolute;
    top: 128px; left: 0; right: 0;
    text-align: center;
    color: var(--ink-red);
    font-weight: 700;
    font-size: 24px;
  }
  .appt-row {
    position: absolute;
    left: 70px; right: 70px;
    display: flex;
    align-items: flex-end;
    gap: 10px;
    color: var(--ink-red);
    font-weight: 700;
    font-size: 20px;
  }
  .appt-row.row-date { top: 172px; }
  .appt-row.row-with { top: 214px; }
  .fill-line {
    flex: 1;
    border-bottom: 3px dotted var(--dot-blue);
    margin-bottom: 5px;
  }
  .appt-notice {
    position: absolute;
    top: 268px; left: 50px; right: 50px;
    text-align: center;
    font-weight: 700;
    font-size: 17px;
    line-height: 1.4;
  }
  .appt-notice .lead { color: var(--ink-red); }
  .appt-notice .tail { color: var(--ink-blue); }

  /* Front side: contact card */
  .card-front { top: 469px; }
  .front-art { position: absolute; inset: 0; width: 100%; height: 100%; }
  .front-brand {
    position: absolute;
    left: 40px; top: 130px;
    width: 300px;
    display: flex;
    align-items: center;
    gap: 14px;
  }
  .front-brand .brand-dot { background: var(--teal); width: 70px; height: 70px; flex: none; }
  .front-brand .brand-name {
    color: var(--white);
    font-size: 20px;
    line-height: 1.25;
    letter-spacing: 1px;
  }
  .contact {
    position: absolute;
    right: 34px; top: 34px;
    text-align: right;
    color: var(--white);
  }
  .doctors { font-weight: 600; font-size: 22px; line-height: 1.3; }
  .address { margin-top: 16px; font-size: 17px; line-height: 1.3; }
  .lines { margin-top: 14px; font-size: 17px; line-height: 1.4; }
  .line { display: flex; justify-content: flex-end; align-items: center; gap: 8px; }
  .line svg { width: 15px; height: 15px; flex: none; }
</style>
</head>
<body>

<section class="card card-back" aria-label="Appointment card, back side">
  <div class="brand">
    <span class="brand-dot"></span>
    <span class="brand-name">Voskamp Family Dentistry</span>
  </div>
  <h2 class="appt-title">Appointment</h2>
  <div class="appt-row row-date">
    <span>Date</span><span class="fill-line"></span>
    <span>Time</span><span class="fill-line"></span>
  </div>
  <div class="appt-row row-with">
    <span>With</span><span class="fill-line"></span>
  </div>
  <p class="appt-notice">
    <span class="lead">If unable to keep your appointment, please give 24-48 hours</span><br>
    <span class="tail">notice in order to avoid broken appointment fee.</span>
  </p>
</section>

<section class="card card-front" aria-label="Business card, front side">
  <svg class="front-art" viewBox="0 0 680 389" preserveAspectRatio="none" aria-hidden="true">
    <defs>
      <linearGradient id="sky" x1="0" y1="0" x2="0" y2="1">
        <stop offset="0" stop-color="#9cc3ea"/>
        <stop offset="1" stop-color="#1d5aa6"/>
      </linearGradient>
    </defs>
    <rect width="680" height="389" fill="url(#sky)"/>
    <path d="M0 0 H410 C480 110 460 290 270 389 H0 Z" fill="#e3262f"/>
    <path d="M0 0 H418 C478 90 470 170 440 230 C420 170 400 80 360 0 Z" fill="#14a889"/>
    <path d="M0 0 H398 C462 110 440 285 255 389 H0 Z" fill="#000000"/>
  </svg>

  <div class="front-brand">
    <span class="brand-dot"></span>
    <span class="brand-name">Voskamp Family Dentistry</span>
  </div>

  <div class="contact">
    <p class="doctors">Gerald K. Voskamp, DDS<br>Marvin R Duchene, DDS</p>
    <p class="address">418 Birchwood Lane<br>Portland, CT 06591</p>
    <div class="lines">
      <p class="line">860 517 4093
        <svg viewBox="0 0 16 16" aria-label="Phone"><path fill="#fff" d="M3 1l3 3-1.5 2c1 2 2.5 3.5 4.5 4.5L11 9l3 3-2 3C6 14 2 10 1 3z"/></svg>
      </p>
      <p class="line">860 517 4094
        <svg viewBox="0 0 16 16" aria-label="Fax"><rect x="2" y="5" width="12" height="8" rx="1" fill="#fff"/><rect x="4" y="1" width="8" height="5" fill="#fff"/><rect x="5" y="8" width="6" height="1.5" fill="#1d5aa6"/></svg>
      </p>
      <p class="line">WWW.BrightArcDental.Com
        <svg viewBox="0 0 16 16" aria-label="Website"><circle cx="8" cy="8" r="7" fill="#fff"/><path d="M1 8h14M8 1c3 3 3 11 0 14M8 1c-3 3-3 11 0 14" stroke="#1d5aa6" fill="none"/></svg>
      </p>
      <p class="line">Office hours by appointment</p>
    </div>
  </div>
</section>

</body>
</html>
```